We Need a GREAT Looking Sales Flyer!

Our small, boutique fitness facility needs a new flyer which highlights a new entry level fitness program that we are launching.

The flyer should be visually appealing as we will be handing a full color version to the potential member during our sales process.

I have attached:
- a word document which includes text
-Photos that can be used. Not all need to be used. These are to be used as you feel appropriate
- Our Logo

```html
<!DOCTYPE html>
<html lang="en">
<head>
<meta charset="utf-8">
<title>The Ultimate Kick Start – Pulsewell</title>
<link rel="stylesheet" href="https://fonts.googleapis.com/css2?family=Anton&family=Oswald:wght@300;400;500;600;700&family=Permanent+Marker&family=Rubik+Dirt&display=swap">
<style>
  :root {
    --backdrop: #5b5b57;
    --ink: #0c0c0c;
    --white: #ffffff;
    --yellow: #f5ea14;
    --sky: #1fb9ec;
    --photo-light: #d9d64a;
    --photo-mid: #9c9a3a;
    --photo-dark: #4a4a2a;
  }
  * { margin: 0; padding: 0; box-sizing: border-box; }
  html, body { width: 1113px; height: 1200px; overflow: hidden; }
  body { background: var(--backdrop); position: relative; }

  .flyer {
    position: absolute; left: 106px; top: 18px;
    width: 900px; height: 1164px;
    background: var(--sky); overflow: hidden;
    box-shadow: 0 10px 30px rgba(0,0,0,.35);
  }
  .hero-photo {
    position: absolute; left: 0; top: 0; width: 900px; height: 760px;
    background:
      radial-gradient(ellipse at 75% 35%, var(--photo-light) 0%, transparent 45%),
      linear-gradient(160deg, var(--photo-mid) 0%, var(--photo-light) 40%, var(--photo-dark) 100%);
  }
  .splash { position: absolute; left: 0; width: 900px; }
  .splash--dark { top: 640px; height: 220px; }
  .splash--sky { top: 800px; height: 120px; }

  .headline {
    position: absolute; left: 40px; top: 70px; width: 820px; text-align: center;
    font-family: "Rubik Dirt", "Anton", sans-serif; font-weight: 400;
    color: var(--white); line-height: 1; font-size: 104px;
    white-space: nowrap;
    text-shadow: 0 4px 0 rgba(0,0,0,.55), 0 0 12px rgba(0,0,0,.4);
    transform: rotate(-6deg);
  }
  .proof {
    position: absolute; left: 230px; top: 310px; width: 520px; text-align: center;
    font-family: "Permanent Marker", "Oswald", sans-serif;
    color: var(--white); font-size: 26px; line-height: 1.1;
    white-space: nowrap;
    text-shadow: 0 2px 4px rgba(0,0,0,.7);
    transform: rotate(-6deg);
  }
  .program-name {
    position: absolute; left: 0; width: 900px; top: 470px; text-align: center;
    font-family: "Anton", sans-serif; font-weight: 400; color: var(--white);
    font-size: 96px; line-height: 1.02; text-transform: uppercase;
    -webkit-text-stroke: 2px var(--ink);
    text-shadow: 6px 6px 0 var(--ink);
    transform: rotate(-4deg);
  }
  .promise {
    position: absolute; left: 0; width: 900px; top: 700px; text-align: center;
    font-family: "Oswald", sans-serif; font-weight: 600;
    color: var(--yellow); font-size: 40px; line-height: 1.2;
  }
  .get-started {
    position: absolute; left: 0; width: 900px; top: 770px; text-align: center;
    font-family: "Oswald", sans-serif; font-weight: 600;
    color: var(--white); font-size: 30px; line-height: 1.2; text-transform: uppercase;
  }
  .price-tag {
    position: absolute; left: 205px; top: 830px; width: 490px; height: 42px;
    background: var(--yellow); border-radius: 12px;
    display: flex; align-items: center; justify-content: center; gap: 16px;
    font-family: "Oswald", sans-serif; font-weight: 600; font-size: 24px;
    color: var(--ink); text-transform: uppercase; white-space: nowrap;
  }
  .benefits {
    position: absolute; left: 150px; top: 918px; width: 600px; height: 168px;
    border: 1.5px solid var(--white);
    padding-top: 26px; text-align: center;
    font-family: "Oswald", sans-serif; font-weight: 400;
    color: var(--white); font-size: 19px; line-height: 1.32;
  }
  .benefits__title {
    position: absolute; left: 50%; top: -24px; transform: translateX(-50%);
    padding: 0 14px; background: var(--sky);
    font-family: "Oswald", sans-serif; font-weight: 700; font-size: 34px; line-height: 1.2;
    color: var(--yellow); text-transform: uppercase; white-space: nowrap;
  }
  .benefits__list { list-style: none; }
  .brand {
    position: absolute; left: 0; width: 900px; top: 1096px; text-align: center;
    font-family: "Oswald", sans-serif; font-weight: 600;
    font-size: 50px; color: var(--white); line-height: 1;
  }
</style>
</head>
<body>
  <main class="flyer">
    <div class="hero-photo" role="img" aria-label="Group fitness class training with suspension straps in a brightly lit gym"></div>

    <svg class="splash splash--dark" viewBox="0 0 900 220" preserveAspectRatio="none" aria-hidden="true">
      <path fill="#0c0c0c" d="M0 60 L40 48 L70 62 L110 40 L150 55 L200 30 L240 46 L300 20 L350 40 L420 10 L470 32 L540 8 L600 28 L660 12 L720 34 L780 18 L840 40 L900 26 L900 220 L0 220 Z"/>
      <circle cx="60" cy="30" r="5" fill="#0c0c0c"/><circle cx="320" cy="6" r="4" fill="#0c0c0c"/><circle cx="700" cy="10" r="6" fill="#0c0c0c"/>
    </svg>
    <svg class="splash splash--sky" viewBox="0 0 900 120" preserveAspectRatio="none" aria-hidden="true">
      <path fill="#1fb9ec" d="M0 70 L50 52 L90 66 L140 38 L190 58 L250 30 L300 50 L360 24 L420 44 L480 18 L540 40 L600 14 L660 36 L720 10 L780 30 L840 6 L900 20 L900 120 L0 120 Z"/>
      <circle cx="200" cy="18" r="5" fill="#1fb9ec"/><circle cx="520" cy="8" r="4" fill="#1fb9ec"/><circle cx="860" cy="0" r="5" fill="#1fb9ec"/>
    </svg>

    <h1 class="headline">CHANGE<br>BEGINS NOW</h1>
    <p class="proof">THE FITNESS PROGRAM THAT IS<br>RESPONSIBLE FOR TRANSFORMING<br>OVER 924 LIVES!</p>

    <h2 class="program-name">The Ultimate<br>Kick Start</h2>

    <p class="promise">The Life That You Envision IS POSSIBLE!</p>
    <p class="get-started">Get started for</p>
    <div class="price-tag">
      <span>$199 (crossed out)</span><span>only $99</span><span>limited time</span>
    </div>

    <section class="benefits">
      <h3 class="benefits__title">What you get</h3>
      <ul class="benefits__list">
        <li>Unlimited Group Training Designed Specifically to Sculpt &amp; Tone the body.</li>
        <li>CUSTOM Meal Plan designed specifically for Your and Your Body Type</li>
        <li>(2) Detailed Body Scans to track results</li>
        <li>Supplement List to accelerate metabolism</li>
        <li>10% off First Supplement Purchase to Kickstart the process</li>
      </ul>
    </section>

    <p class="brand">Pulsewell</p>
  </main>
</body>
</html>
```